Car Import Specialist Needs A Flyer

Need a flyer to describe to list the services we provide and cost of those services. We are based in Melbourne ( Australia) but serve customers from all parts of Australia.

The flyer needs to state the following:

Looking for a Japanese performance car? We can find you the car you want and import it for you at the lowest price - Guaranteed!!!!

Why choose us as your direct import partner?

* Over 15 years industry experience
* Vehicles pre-inspection like no other, carried out by our Japan based staff
* Fully licensed motor car trader / QMB 4417 certified / TEVP certified
* In house compliance center
* Mileage guarantee - Export certificates and auction sheets provided with all cars.

-------------------------------------------------------

We need to have pictures of cars on the flyer. I have added pics of cars that we wish to promote.

```html
<!DOCTYPE html>
<html lang="en">
<head>
<meta charset="utf-8">
<title>Japanese Performance Car Import Flyer</title>
<link rel="stylesheet" href="https://fonts.googleapis.com/css2?family=Bebas+Neue&family=Lato:wght@400;700;900&display=swap">
<style>
  :root {
    --orange: #ec7405;
    --orange-deep: #c85f02;
    --charcoal: #2f2f31;
    --ink: #262626;
    --white: #ffffff;
    --silver-light: #f1f1f1;
    --silver-dark: #8a8a8a;
  }
  * { margin: 0; padding: 0; box-sizing: border-box; }
  html, body { width: 907px; height: 1200px; overflow: hidden; background: var(--charcoal); }
  .flyer {
    position: relative;
    width: 907px;
    height: 1200px;
    overflow: hidden;
    background: var(--charcoal);
    font-family: 'Lato', Arial, sans-serif;
  }
  .hero-photo {
    position: absolute;
    left: 0; top: 0;
    width: 907px; height: 430px;
    background:
      radial-gradient(ellipse 45% 35% at 55% 45%, #e0762a 0%, #b8581a 45%, rgba(184,88,26,0) 75%),
      linear-gradient(180deg, #5d5f66 0%, #9a9ca3 55%, #d9d9dc 80%, #c4c4c7 100%);
  }
  .shapes { position: absolute; left: 0; top: 0; }
  .headline {
    position: absolute;
    right: 112px;
    top: 432px;
    text-align: right;
    font-family: 'Bebas Neue', Impact, sans-serif;
    line-height: 1;
  }
  .headline .lead { display: block; font-size: 48px; color: var(--ink); letter-spacing: 1px; }
  .headline .main { display: block; font-size: 76px; color: var(--white); letter-spacing: 1px; margin-top: 2px; }
  .tagline {
    position: absolute;
    right: 112px;
    top: 560px;
    width: 300px;
    text-align: right;
    font-size: 21px;
    line-height: 26px;
    color: var(--ink);
  }
  .seal { position: absolute; left: 35px; top: 413px; }
  .why {
    position: absolute;
    left: 49px;
    top: 680px;
    font-size: 28px;
    line-height: 34px;
    font-weight: 700;
    color: var(--orange);
  }
  .benefits {
    position: absolute;
    left: 49px;
    top: 763px;
    width: 820px;
    list-style: none;
    font-size: 20.5px;
    line-height: 26px;
    color: var(--white);
  }
  .benefits li { position: relative; padding-left: 25px; margin-bottom: 6px; }
  .benefits li::before {
    content: "";
    position: absolute;
    left: 0; top: 8px;
    width: 11px; height: 11px;
    border-radius: 50%;
    background: var(--orange);
  }
  .gallery-photo {
    position: absolute;
    top: 982px;
    height: 160px;
    border: 5px solid var(--white);
    border-radius: 34px 10px 34px 10px;
    box-shadow: 0 4px 10px rgba(0,0,0,0.35);
  }
  .sunset-drive { left: 44px; width: 250px; background: linear-gradient(180deg, #6d6670 0%, #d9895a 45%, #3b3437 70%, #55504f 100%); }
  .coastal-road { left: 329px; width: 254px; background: linear-gradient(180deg, #9fb1c7 0%, #6f8a5e 45%, #4c4a48 75%, #7b7875 100%); }
  .silver-coupe { left: 614px; width: 254px; background: radial-gradient(ellipse 60% 40% at 50% 55%, #a8acb2 0%, #d7d9dc 60%, #ffffff 100%); }
</style>
</head>
<body>
<main class="flyer">
  <div class="hero-photo" role="img" aria-label="Orange Japanese sports coupe in a grey studio"></div>

  <svg class="shapes" width="907" height="1200" viewBox="0 0 907 1200" aria-hidden="true">
    <polygon points="0,402 907,362 907,650 831,775 0,555" fill="var(--orange)"/>
    <polygon points="907,470 907,650 831,775 780,700" fill="var(--orange-deep)"/>
    <polygon points="470,1200 880,965 907,965 907,1200" fill="var(--orange)"/>
  </svg>

  <svg class="seal" width="232" height="232" viewBox="0 0 232 232" aria-hidden="true">
    <defs>
      <linearGradient id="ring" x1="0" y1="0" x2="1" y2="1">
        <stop offset="0" stop-color="#f7f7f7"/>
        <stop offset="0.5" stop-color="#b9b9b9"/>
        <stop offset="1" stop-color="#6e6e6e"/>
      </linearGradient>
      <radialGradient id="face" cx="0.4" cy="0.35" r="0.7">
        <stop offset="0" stop-color="#ffffff"/>
        <stop offset="1" stop-color="#c9c9c9"/>
      </radialGradient>
      <path id="ring-path" d="M116,116 m-88,0 a88,88 0 1,1 176,0 a88,88 0 1,1 -176,0"/>
    </defs>
    <circle cx="116" cy="116" r="112" fill="url(#ring)"/>
    <circle cx="116" cy="116" r="104" fill="#1d1d1d"/>
    <circle cx="116" cy="116" r="100" fill="url(#ring)"/>
    <circle cx="116" cy="116" r="74" fill="url(#face)" stroke="#7a7a7a" stroke-width="2"/>
    <text font-family="Lato, Arial, sans-serif" font-weight="900" font-size="17" fill="#1d1d1d" letter-spacing="1">
      <textPath href="#ring-path" startOffset="0">GUARANTEED!!! · GUARANTEED!!! · GUARANTEED!!! ·</textPath>
    </text>
    <text x="116" y="113" text-anchor="middle" font-family="Lato, Arial, sans-serif" font-weight="900" font-size="30" fill="#1d1d1d">LOWEST</text>
    <text x="116" y="152" text-anchor="middle" font-family="Lato, Arial, sans-serif" font-weight="900" font-size="42" fill="#1d1d1d">PRICE</text>
  </svg>

  <h1 class="headline">
    <span class="lead">Looking for a Japanese</span>
    <span class="main">Performance Car?</span>
  </h1>
  <p class="tagline">We can find you the car you want and import it for you at the lowest price</p>

  <h2 class="why">Why choose us as your direct<br>import partner?</h2>
  <ul class="benefits">
    <li>Over 15 years industry experience</li>
    <li>Vehicles pre-inspection like no other, carried out by our Japan based staff</li>
    <li>Fully licensed motor car trader / QMB 4417 certified / TEVP certified</li>
    <li>In house compliance center</li>
    <li>Mileage guarantee - Export certificates and auction sheets provided with<br>all cars</li>
  </ul>

  <div class="gallery-photo sunset-drive" role="img" aria-label="Sports car driving on an open road at sunset"></div>
  <div class="gallery-photo coastal-road" role="img" aria-label="White hatchback speeding along a winding road"></div>
  <div class="gallery-photo silver-coupe" role="img" aria-label="Silver coupe seen from the rear on a white background"></div>
</main>
</body>
</html>
```